Design a Mobile App for Landscape Businesses

This project is to design the first three screens for a mobile app for Landscape and Lawncare businesses. This app will serve as a directory for homeowners to locate landscape and lawn care businesses and for landscape businesses and contractors to run their business. See the attached PDF for more information and example
Here is the link to the description https://lnkshrt.example/q7Tz3K

Target Market(s)

Landscape and lawn care business, gardeners, home owners

Industry/Entity Type

Landscape Gardening

Logo Text

Velmarigo

Colors

Designer to choose colors to be used in the design.

```html
<!DOCTYPE html>
<html lang="en">
<head>
<meta charset="utf-8">
<title>Velmarigo – Lawncare businesses</title>
<link href="https://fonts.googleapis.com/css2?family=Arimo:wght@400;500;700&display=swap" rel="stylesheet">
<style>
  :root {
    --green: #3f7a35;
    --green-dark: #2f6a2a;
    --green-light: #4e8f43;
    --white: #ffffff;
    --ink: #1c1c1c;
    --muted: #7a7a7a;
    --phone: #3c7d33;
    --map: #e9e6df;
  }
  * { box-sizing: border-box; margin: 0; padding: 0; }
  html, body { width: 675px; height: 1200px; overflow: hidden; background: var(--white); }
  body { font-family: "Arimo", Helvetica, Arial, sans-serif; position: relative; color: var(--ink); }

  .app-header {
    position: absolute; left: 0; top: 0; width: 675px; height: 124px;
    background: linear-gradient(180deg, #3b7d33 0%, var(--green-dark) 100%);
    color: var(--white);
  }
  .status-bar { position: absolute; left: 14px; right: 14px; top: 14px; height: 26px; display: flex; align-items: center; font-size: 20px; }
  .status-bar .signal { display: flex; gap: 3px; margin-right: 8px; }
  .status-bar .signal span { width: 10px; height: 10px; border-radius: 50%; background: var(--white); }
  .status-bar .signal span.off { background: none; border: 1.5px solid var(--white); }
  .status-bar .right { margin-left: auto; display: flex; align-items: center; gap: 8px; }
  .battery { width: 42px; height: 18px; border: 2px solid var(--white); border-radius: 4px; padding: 2px; }
  .battery i { display: block; width: 100%; height: 100%; background: var(--white); border-radius: 1px; }

  .header-title { position: absolute; left: 0; right: 0; top: 66px; text-align: center; font-size: 27px; font-weight: 500; letter-spacing: 0.3px; }
  .header-icon { position: absolute; top: 68px; }

  .photo-grid { position: absolute; left: 0; top: 124px; width: 675px; height: 319px; display: grid; grid-template-columns: repeat(3, 1fr); grid-template-rows: repeat(2, 1fr); gap: 1px; background: #fff; }
  .photo { width: 100%; height: 100%; }
  .photo-add { display: flex; align-items: center; justify-content: center; background: #3f7d33; }

  .services-title { position: absolute; left: 0; right: 0; top: 472px; text-align: center; font-size: 27px; font-weight: 400; }
  .service-tag {
    position: absolute; height: 48px; background: var(--green); color: var(--white);
    border-radius: 3px; font-size: 15px; display: flex; align-items: center; justify-content: center;
  }

  .map-area { position: absolute; left: 0; top: 738px; width: 675px; height: 349px; background: linear-gradient(160deg, #ebe8e1 0%, #e3e2d8 60%, #e9e5dc 100%); }
  .address-card {
    position: absolute; left: 84px; top: 784px; width: 501px; height: 160px; background: var(--white);
    border-radius: 3px; box-shadow: 0 2px 10px rgba(0,0,0,0.18); text-align: center; padding-top: 32px;
  }
  .address-card h3 { font-size: 18px; font-weight: 400; margin-bottom: 8px; }
  .address-card p { font-size: 13.5px; color: var(--muted); line-height: 24px; }
  .address-card .phone { font-size: 18px; color: var(--phone); margin-top: 4px; letter-spacing: 0.5px; }

  .quote-button {
    position: absolute; left: 51px; top: 980px; width: 577px; height: 74px; background: var(--green);
    border-radius: 3px; color: var(--white); font-size: 22px; font-weight: 500; letter-spacing: 0.6px;
    display: flex; align-items: center; justify-content: center;
  }

  .tab-bar { position: absolute; left: 0; top: 1087px; width: 675px; height: 113px; background: linear-gradient(180deg, var(--green-light) 0%, #3a7631 100%); }
  .tab-icon { position: absolute; top: 1122px; }
  .tab-center {
    position: absolute; left: 286px; top: 1093px; width: 100px; height: 100px; border-radius: 50%;
    background: #4f8f45; border: 2px solid rgba(255,255,255,0.9); box-shadow: 0 3px 8px rgba(0,0,0,0.3);
    display: flex; align-items: center; justify-content: center;
  }
</style>
</head>
<body>

<header class="app-header">
  <div class="status-bar">
    <div class="signal"><span></span><span></span><span></span><span></span><span class="off"></span></div>
    <span>Carrier</span>
    <svg width="22" height="16" viewBox="0 0 22 16" style="margin-left:8px"><path d="M2 6a13 13 0 0 1 18 0M5 9a8.5 8.5 0 0 1 12 0M8 12a4 4 0 0 1 6 0" stroke="#fff" stroke-width="2" fill="none" stroke-linecap="round"/><circle cx="11" cy="14.5" r="1.5" fill="#fff"/></svg>
    <div class="right">
      <svg width="20" height="20" viewBox="0 0 20 20"><circle cx="10" cy="10" r="8" stroke="#fff" stroke-width="1.8" fill="none"/><rect x="6.5" y="9" width="7" height="5" fill="#fff"/><path d="M8 9V7.5a2 2 0 0 1 4 0V9" stroke="#fff" stroke-width="1.5" fill="none"/></svg>
      <span>100%</span>
      <div class="battery"><i></i></div>
    </div>
  </div>
  <svg class="header-icon" style="left:18px" width="32" height="28" viewBox="0 0 32 28" fill="#fff"><rect x="0" y="3" width="5" height="4"/><rect x="9" y="3" width="23" height="3"/><rect x="0" y="12" width="5" height="4"/><rect x="9" y="12" width="23" height="3"/><rect x="0" y="21" width="5" height="4"/><rect x="9" y="21" width="23" height="3"/></svg>
  <h1 class="header-title">Lawncare businesses</h1>
  <svg class="header-icon" style="left:632px" width="26" height="26" viewBox="0 0 26 26"><path d="M11 2h4l.7 3 2.4 1.2 2.7-1.6 2.8 2.8-1.6 2.7L23 12.5l3 .5v4l-3 .7-1 2.4 1.6 2.7-2.8 2.8-2.7-1.6-2.4 1-.7 3h-4l-.7-3-2.4-1-2.7 1.6-2.8-2.8 1.6-2.7-1-2.4L0 17V13l3-.5 1-2.4-1.6-2.7 2.8-2.8 2.7 1.6L10.3 5z" transform="scale(.92) translate(1 0)" stroke="#fff" stroke-width="1.8" fill="none" stroke-linejoin="round"/><circle cx="13" cy="13.5" r="4" stroke="#fff" stroke-width="1.8" fill="none"/></svg>
</header>

<section class="photo-grid">
  <div class="photo" role="img" aria-label="Bare feet resting on fresh green grass" style="background:linear-gradient(135deg,#b8c86a,#6d9a2c)"></div>
  <div class="photo photo-add" role="img" aria-label="Add photo tile over a green forest">
    <svg width="32" height="32" viewBox="0 0 32 32"><path d="M16 2v28M2 16h28" stroke="#fff" stroke-width="4"/></svg>
  </div>
  <div class="photo" role="img" aria-label="Residents and carers outside a sunny apartment building" style="background:linear-gradient(180deg,#c9d8e6,#e8d9a8 60%,#9aa67a)"></div>
  <div class="photo" role="img" aria-label="Wide green lawn under a blue sky" style="background:linear-gradient(180deg,#bcd3e8 0%,#dfe9ee 45%,#6f9e3a 60%,#8cc43e 100%)"></div>
  <div class="photo" role="img" aria-label="Smiling gardener holding freshly picked plants" style="background:linear-gradient(160deg,#5a6a45,#3d5a2a 60%,#4e7a2e)"></div>
  <div class="photo" role="img" aria-label="Hand brushing through tall grass at sunset" style="background:linear-gradient(135deg,#f2c46a,#b6b84e 55%,#7d9a3a)"></div>
</section>

<h2 class="services-title">Services Offered</h2>

<div class="service-tag" style="left:28px;top:528px;width:236px">Shrubs, Hedges &amp; Bushes</div>
<div class="service-tag" style="left:272px;top:528px;width:146px">Yard Cleaning</div>
<div class="service-tag" style="left:426px;top:528px;width:221px">Landscape Construction</div>
<div class="service-tag" style="left:29px;top:588px;width:192px">Residential Services</div>
<div class="service-tag" style="left:231px;top:588px;width:135px">Yard Debris</div>
<div class="service-tag" style="left:375px;top:588px;width:237px">Landscape Maintenance</div>
<div class="service-tag" style="left:28px;top:648px;width:193px">Irrigation Installation</div>
<div class="service-tag" style="left:230px;top:648px;width:194px">Commerical Services</div>
<div class="service-tag" style="left:432px;top:648px;width:193px">See More Services</div>

<div class="map-area" role="img" aria-label="Street map showing the business location and surrounding suburbs"></div>

<div class="address-card">
  <h3>Address</h3>
  <p>Lorem Ipsum is simply dummy text of the printing and typeset-<br>ting industry. Lorem Ipsum has been the industry's</p>
  <div class="phone">(555) 014 2736</div>
</div>

<div class="quote-button">REQUEST A QUOTE</div>

<nav class="tab-bar"></nav>
<svg class="tab-icon" style="left:60px" width="38" height="30" viewBox="0 0 38 30" fill="#fff"><rect y="2" width="38" height="3"/><rect y="13" width="38" height="3"/><rect y="24" width="38" height="3"/></svg>
<svg class="tab-icon" style="left:182px" width="42" height="36" viewBox="0 0 42 36" fill="none" stroke="#fff" stroke-width="1.8"><circle cx="16" cy="11" r="7"/><path d="M3 34c0-8 6-12 13-12s13 4 13 12z"/><path d="M24 5a7 7 0 1 1 4 13M31 22c5 1 8 5 8 12h-8"/></svg>
<div class="tab-center">
  <svg width="40" height="54" viewBox="0 0 40 54" fill="none" stroke="#fff" stroke-width="2.2"><path d="M20 52C8 36 3 27 3 19a17 17 0 0 1 34 0c0 8-5 17-17 33z"/><circle cx="20" cy="19" r="6"/></svg>
</div>
<svg class="tab-icon" style="left:464px" width="36" height="38" viewBox="0 0 36 38" fill="none" stroke="#fff" stroke-width="1.8"><rect x="2" y="5" width="32" height="31"/><path d="M2 12h32M9 1v7M27 1v7"/><path d="M8 17h20v14H8zM8 24h20M13 17v14M18 17v14M23 17v14M8 20.5h20M8 27.5h20" stroke-width="1.2"/></svg>
<svg class="tab-icon" style="left:577px" width="40" height="40" viewBox="0 0 40 40" fill="none" stroke="#fff" stroke-width="2.2"><circle cx="17" cy="17" r="14"/><path d="M27 27l11 11"/></svg>

</body>
</html>
```